Interior Decorator Website - Tiny Meadow

I am an interior decorator (mainly for children's rooms) - my blog is www.tinymeadow1.quillnest.net - I already have a logo which I'm happy with so you would need to work around this. I am wanting to create a modern chic looking website to showcase my completed rooms. The look I want is clean, fresh with colors grey, white, and grey linen - some examples from Pictoranda (just put number into the keyword search) ....

Image ID: 31927485
Image ID: 47018263

Obviously I would need functionality that would allow me to go into the backend myself and change photo's and categories and sub categories. I also need to be able to link to my blog. I am happy to have the web design satisfied first and then negotiate a sum for coding after.

A website that I'm fond of for it's catergories and feel is http://www.velomarsh.com/portfolio/detail/pink_green_modern for the look and functionality and catergories (although for my front page I would probably just want my logo and then go into something like this for the second page).
I also LOVE LOVE LOVE the look and feel of wren and tobin -http://wrenandtobin.net/ - I like how it has 3 aspirational photo's to set the mood. Some examples (and you may be able to find some nicer ones) for this would be a pic of a child in black and white (I have attached two cute ones of one of my kids) then a cool mobile - http://static.quarvix.net/img/hangingm/W300-H300-Bffffff/F/drumbelo149.jpg, and one other? maybe a knitted pouf http://4.img.quillnest.net/_kaTrW_BmeQ7/HJqRvPdWzkA/AAAAAAAAF8C/TnwLbeuXaRp/s1600/knitted+grey.png - I also love the chevron stripe on their blog - maybe I could incorporate this in white and grey neat to my logo? http://blog.wrenandtobin.net/
I also like the look of this website -http://www.plumkidhaven.com:80/index.jsp?link=global_logo

I will have ONLY professional photo's up on the website whereas my blog will be more casual with photo's that I have taken. I want the overall feel to be CHIC and MODERN.

Industry/Entity Type

Interior

Requirements
Must have
• CMS - either Joomla or Wordpress
Home PAGE (Tiny Meadow Logo) + PAGE 1 (more aspirational with pics)

CATERGORIES REQUIRED
1. ABOUT US
2. KIDS SPACES
3. ADULT SPACES
4. COMMERCIAL
5. DESIGN SERVICES
4. BLOG
5. PRESS
6. CONTACT
Nice to have
• PLEASE NOTE: Happy to just have Web Design first and then negotiate price for coding after.

```html
<!DOCTYPE html>
<html lang="en">
<head>
<meta charset="utf-8">
<title>Tiny Meadow – Interior Decorating</title>
<link rel="stylesheet" href="https://fonts.googleapis.com/css2?family=Open+Sans:wght@300;400;600&display=swap">
<style>
:root{
  --header:#909193;
  --linen:#dcdcdc;
  --linen-thread-dark:rgba(120,120,120,.16);
  --linen-thread-light:rgba(255,255,255,.35);
  --panel:#f1f1f1;
  --panel-edge:#ffffff;
  --dash:#c8c8c8;
  --ink:#3a3a3a;
  --soft-ink:#5a5a5a;
  --bar:#8a8a8a;
  --white:#ffffff;
  --footer:#8c8c8e;
}
*{box-sizing:border-box;margin:0;padding:0}
html,body{width:1200px;height:2677px;overflow:hidden}
body{
  position:relative;font-family:"Open Sans",Arial,sans-serif;color:var(--ink);
  background-color:var(--linen);
  background-image:
    repeating-linear-gradient(0deg,var(--linen-thread-dark) 0 1px,transparent 1px 3px),
    repeating-linear-gradient(90deg,var(--linen-thread-light) 0 1px,transparent 1px 4px),
    repeating-linear-gradient(90deg,var(--linen-thread-dark) 0 1px,transparent 1px 7px),
    repeating-linear-gradient(0deg,var(--linen-thread-light) 0 1px,transparent 1px 5px);
}
.abs{position:absolute}
.textured{
  background-image:
    repeating-linear-gradient(0deg,rgba(0,0,0,.05) 0 1px,transparent 1px 3px),
    repeating-linear-gradient(90deg,rgba(255,255,255,.06) 0 1px,transparent 1px 4px);
}

.site-header{left:0;top:0;width:1200px;height:178px;background-color:var(--header)}
.brand{left:32px;top:62px;display:flex;align-items:center;gap:24px}
.brand-dot{width:56px;height:56px;border-radius:50%;background:var(--white)}
.brand-name{font-weight:300;font-size:36px;letter-spacing:5px;color:var(--white)}
.search{left:905px;top:72px;width:258px;height:34px}
.search-field{position:absolute;left:0;top:0;width:238px;height:34px;background:#b6b7b9;border:1px solid #a3a4a6}
.search svg{position:absolute;right:0;top:2px}

.main-nav{left:33px;top:205px;width:1132px;height:54px;background-color:#929295;border:2px solid #a9a9ac;display:flex;justify-content:space-between;align-items:center;padding:0 20px}
.main-nav a,.footer-nav a{color:var(--white);text-decoration:none;text-transform:uppercase;font-weight:400}
.main-nav a{font-size:20px}

.hero{left:33px;top:279px;width:1132px;height:569px;background:var(--white)}
.hero-photo{left:16px;top:13px;width:1104px;height:543px;background:radial-gradient(ellipse at 55% 45%,#a9a9a9 0%,#8a8a8a 35%,#5e5e5e 70%,#4a4a4a 100%)}
.hero-caption{left:16px;top:446px;width:1104px;height:110px;background:rgba(45,45,45,.55);color:var(--white);font-weight:300;font-size:29px;line-height:44px;padding:12px 40px}

.panel{background:var(--panel);border:6px solid var(--panel-edge);outline:1px solid #c9c9c9}
.panel::after{content:"";position:absolute;inset:4px;border:1px dashed var(--dash);pointer-events:none}
.panel-title{position:absolute;left:28px;font-weight:300;font-size:26px;color:var(--ink)}

.about{left:38px;top:870px;width:404px;height:480px}
.avatar{left:28px;top:72px;width:122px;height:132px;background:radial-gradient(circle at 50% 45%,#bdbdbd,#8e8e8e);border:2px solid #ffffff}
.about-name{left:180px;top:92px;font-size:21px;line-height:30px;font-weight:400;color:var(--ink)}
.about-bio{left:28px;top:232px;width:342px;font-size:13px;line-height:26px;color:var(--soft-ink)}
.about-bio a{color:var(--soft-ink)}
.profile-link{right:28px;top:428px;font-size:13px;color:var(--soft-ink);text-decoration:underline}

.subscribe{left:38px;top:1376px;width:404px;height:241px}
.sub-label{left:28px;top:88px;font-size:13px;color:var(--soft-ink)}
.sub-field{left:28px;top:116px;width:333px;height:34px;background:#fafafa;border:1px solid #cfcfcf}
.sub-button{left:134px;top:180px;width:121px;height:30px;background:var(--bar);color:var(--white);font-size:17px;text-align:center;line-height:30px}

.partners{left:38px;top:1655px;width:404px;height:256px}
.badge-a{left:23px;top:85px;width:118px;height:118px;background:#f7f7f7;border:1px solid #dcdcdc}
.badge-b{left:161px;top:85px;width:203px;height:118px;background:#ffffff;border:1px solid #dcdcdc}

.join{left:38px;top:1940px;width:404px;height:330px}
.members{left:28px;top:80px;width:333px;font-size:13px;color:var(--soft-ink);display:flex;justify-content:space-between}
.member-grid{left:28px;top:101px;width:333px;height:176px;background:#ffffff;border:1px solid #d2d2d2;display:grid;grid-template-columns:repeat(7,34px);gap:13px 11px;padding:16px 12px;align-content:start}
.member-grid span{width:34px;height:34px;background:#b4b4b4}
.member-grid span:nth-child(3n){background:#c9aaa2}
.member-grid span:nth-child(4n){background:#a3a9b0}
.member-grid span:nth-child(5n){background:#d6cbb6}
.signin{left:28px;top:290px;font-size:13px;color:var(--ink)}

.post{width:691px}
.post-one{left:475px;top:870px;height:751px}
.post-two{left:475px;top:1655px;height:749px}
.post-title{position:absolute;left:30px;top:34px;font-weight:300;font-size:27px;color:var(--ink)}
.post-date{position:absolute;right:30px;top:26px;width:200px;height:28px;background:var(--bar);color:var(--white);font-size:13px;text-align:center;line-height:28px}
.post-photo{position:absolute;left:30px;top:89px;width:600px;height:400px}
.post-one .post-photo{background:radial-gradient(ellipse at 45% 60%,#e3bcc3 0%,#cdb3b5 40%,#a9b4b1 100%)}
.post-two .post-photo{background:radial-gradient(ellipse at 50% 40%,#f6f4f2 0%,#e6e1dc 50%,#cbbcae 100%)}
.post-text{position:absolute;left:30px;top:522px;width:600px;font-size:13px;line-height:27px;color:var(--soft-ink)}
.post-meta{position:absolute;left:30px;top:700px;width:600px;height:30px;background:var(--bar);color:var(--white);font-size:13.5px;display:flex;justify-content:space-between;align-items:center;padding:0 12px}

.site-footer{left:0;top:2482px;width:1200px;height:195px;background-color:var(--footer)}
.footer-nav{left:0;top:28px;width:1200px;display:flex;justify-content:center;gap:30px}
.footer-nav a{font-size:16px}
.social{left:492px;top:84px;display:flex;gap:8px}
.social span{width:32px;height:32px;background:#d4d4d6;border-radius:3px}
.copyright{left:0;top:142px;width:1200px;text-align:center;color:var(--white);font-size:14px}
</style>
</head>
<body>

<header class="site-header textured abs">
  <div class="brand abs"><span class="brand-dot"></span><span class="brand-name">tiny meadow</span></div>
  <div class="search abs">
    <div class="search-field"></div>
    <svg width="30" height="30" viewBox="0 0 30 30"><circle cx="12" cy="12" r="9" fill="none" stroke="#222" stroke-width="3.5"/><line x1="18.5" y1="18.5" x2="27" y2="27" stroke="#222" stroke-width="4.5" stroke-linecap="round"/></svg>
  </div>
</header>

<nav class="main-nav textured abs">
  <a href="#">About Us</a><a href="#">Kids Spaces</a><a href="#">Adult Spaces</a><a href="#">Commercial</a><a href="#">Design Services</a><a href="#">Blog</a><a href="#">Press</a><a href="#">Contact</a>
</nav>

<section class="hero abs">
  <div class="hero-photo abs" role="img" aria-label="Black and white portrait of a smiling child with leafy background"></div>
  <p class="hero-caption abs">Tiny Meadow Interior Decorating specialises in creating fabulous and<br>functional children's bedrooms</p>
</section>

<aside>
  <section class="panel about abs">
    <h2 class="panel-title" style="top:26px">About Me</h2>
    <div class="avatar abs" role="img" aria-label="Profile photo of the decorator"></div>
    <p class="about-name abs">Tiny Meadow<br>Elmbrook, Victoria,<br>Australia</p>
    <p class="about-bio abs">Tiny Meadow Interior Decorating specialises in creating fabulous and functional children's bedrooms. Tiny Meadow charges $105.00 per hour and can work to any room budget. Please contact me via email on:<br><a href="#">hello@tinymeadow.net</a></p>
    <a class="profile-link abs" href="#">View my complete profile</a>
  </section>

  <section class="panel subscribe abs">
    <h2 class="panel-title" style="top:30px">Subscribe Newsletter</h2>
    <p class="sub-label abs">Enter your email address:</p>
    <div class="sub-field abs"></div>
    <div class="sub-button abs">Subscribe</div>
  </section>

  <section class="panel partners abs">
    <h2 class="panel-title" style="top:30px">Our Partners</h2>
    <div class="badge-a abs" role="img" aria-label="Partner badge"></div>
    <div class="badge-b abs" role="img" aria-label="Partner badge"></div>
  </section>

  <section class="panel join abs">
    <h2 class="panel-title" style="top:30px">Join this site</h2>
    <div class="members abs"><span>Members (28)</span><span>More »</span></div>
    <div class="member-grid abs" role="img" aria-label="Grid of member profile pictures">
      <span></span><span></span><span></span><span></span><span></span><span></span><span></span>
      <span></span><span></span><span></span><span></span><span></span><span></span><span></span>
      <span></span><span></span><span></span><span></span><span></span><span></span><span></span>
    </div>
    <p class="signin abs">Already a member? Sign in</p>
  </section>
</aside>

<main>
  <article class="panel post post-one abs">
    <h2 class="post-title">Princess Ivy</h2>
    <div class="post-date">Monday, 14 November 2011</div>
    <div class="post-photo" role="img" aria-label="Baby sitting in a pink egg chair in a patterned nursery"></div>
    <p class="post-text">I have to say that Ivy is one lucky bub - her room is like a mini palace! The wallpaper I chose (which I'm completely in love with) gave me so much inspiration for the rest of the room - I love how it all turned out and especially love the vibrant accent color I chose - orange. We had some wallpaper left over from the main wall so I decided to wallpaper the panels in the cupboards which gave such a cohesive feeling in the room. My favourite pieces are the orange cuckoo clock, chevron pillow, mini egg chair and chandelier. .</p>
    <div class="post-meta"><span>Posted by Tiny Meadow at 6:13 PM</span><span>2 comments</span></div>
  </article>

  <article class="panel post post-two abs">
    <h2 class="post-title">Mira's Growing Up</h2>
    <div class="post-date">Monday, 14 November 2011</div>
    <div class="post-photo" role="img" aria-label="Bright girl's bedroom with white bed, world map wall decal and wooden rocking horse"></div>
    <p class="post-text">I have to say that Ivy is one lucky bub - her room is like a mini palace! The wallpaper I chose (which I'm completely in love with) gave me so much inspiration for the rest of the room - I love how it all turned out and especially love the vibrant accent color I chose - orange. We had some wallpaper left over from the main wall so I decided to wallpaper the panels in the cupboards which gave such a cohesive feeling in the room. My favourite pieces are the orange cuckoo clock, chevron pillow, mini egg chair and chandelier. .</p>
    <div class="post-meta"><span>Posted by Tiny Meadow at 6:13 PM</span><span>2 comments</span></div>
  </article>
</main>

<footer class="site-footer textured abs">
  <nav class="footer-nav abs">
    <a href="#">About Us</a><a href="#">Kids Spaces</a><a href="#">Adult Spaces</a><a href="#">Commercial</a><a href="#">Design Services</a><a href="#">Blog</a><a href="#">Press</a><a href="#">Contact</a>
  </nav>
  <div class="social abs"><span></span><span></span><span></span><span></span></div>
  <p class="copyright abs">Copyright @ 2011 tinymeadow.net . All Rights Reserved.</p>
</footer>

</body>
</html>
```